Redesign My Travel Voucher Coupons-Please redesign the flyers I have attached to this brief.

These designs will be catered towards like travel agency vacation stays...luxury resort stays, hotel and airfare getaways, etc. so must have a travel theme but more importantly professional trustworthy appeal...

Please redesign the flyers I have attached to this brief.

I have attached my existing designs. Please use all existing content and elements exactly but make the design much better...also, please keep in mind that these would be full color and printer friendly...

Target Market(s)

Consumers. People receive these vouchers from businesses that run marketing promotions and contests and giveaways. So the look and feel must feel professional and trustworthy but not cheesy and fake.

Industry/Entity Type

Hotel

Requirements
Must have
• Please use all existing content and elements exactly but make the design much better...also, please keep in mind that these would be full color and printer friendly...

MUST HAVE ALL EXISTING CONTENT EXACT NO EXCEPTIONS
Nice to have
• These designs will be catered towards like travel agency vacation stays...luxury resort stays, hotel and airfare getaways, etc. so must have a travel theme but more importantly professional trustworthy appeal...

Should not have

```html
<!DOCTYPE html>
<html lang="en">
<head>
<meta charset="utf-8">
<title>Enjoy Travel Voucher Set</title>
<link href="https://fonts.googleapis.com/css2?family=Paytone+One&family=Montserrat:wght@500;700;800&family=Open+Sans:ital,wght@0,400;0,600;0,700;1,400&display=swap" rel="stylesheet">
<style>
:root{
  --teal:#1a9aa0;
  --teal-dark:#0f6f78;
  --sky:#7fc8e4;
  --sea:#3fa9c9;
  --sand:#efe6d6;
  --yellow:#f6c832;
  --orange:#f08a24;
  --red:#e2492f;
  --purple:#5b3a7a;
  --burgundy:#8a2f4a;
  --navy:#233a6b;
  --ink:#333c44;
  --muted:#6b747c;
  --page:#f2f3f4;
}
*{box-sizing:border-box;margin:0;padding:0}
html,body{width:1200px;height:3000px;overflow:hidden}
body{background:var(--page);font-family:"Open Sans",Arial,sans-serif;color:var(--ink);position:relative}

.flyer{position:absolute;background:#fff;overflow:hidden;box-shadow:0 2px 8px rgba(0,0,0,.12)}
.flyer--main{left:40px;top:30px;width:1120px;height:1150px}

.photo{position:absolute;left:0;top:0;width:100%}
.photo__curve{position:absolute;left:0;bottom:-1px;width:100%}
.enjoy{font-family:"Paytone One",Arial,sans-serif;letter-spacing:4px;line-height:1;
  background:linear-gradient(180deg,var(--yellow),var(--orange) 60%,var(--red));
  -webkit-background-clip:text;background-clip:text;color:transparent;position:absolute}

/* main flyer */
.flyer--main .photo{height:470px;background:linear-gradient(180deg,#bfe4f2 0%,#8fd0e8 35%,#3fa9c9 55%,#7cc9d8 68%,var(--sand) 80%,#f7f1e6 100%)}
.flyer--main .enjoy{left:60px;top:60px;font-size:150px}
.ribbon{position:absolute;display:flex;align-items:center;justify-content:center;font-family:"Montserrat",Arial,sans-serif;font-weight:700;color:var(--teal-dark)}
.flyer--main .ribbon{left:50px;top:235px;width:460px;height:62px;background:var(--yellow);font-size:34px;letter-spacing:1px}
.badge{position:absolute;border-radius:50%;background:var(--teal);color:#fff;display:flex;align-items:center;justify-content:center;text-align:center;font-family:"Montserrat",Arial,sans-serif;font-weight:700}
.flyer--main .badge{right:60px;top:40px;width:230px;height:230px;font-size:15px;line-height:1.35;padding:26px;border:6px solid rgba(255,255,255,.7)}
.badge__big{display:block;font-size:30px}

.section-title{font-family:"Montserrat",Arial,sans-serif;font-weight:800;font-size:15px;color:var(--teal-dark);letter-spacing:1px;margin-bottom:6px}
.body-text{font-size:14px;line-height:1.5}
.col{position:absolute}
.col--plan{left:60px;top:330px;width:470px}
.col--features{left:600px;top:360px;width:460px}
.features{list-style:none;font-family:"Montserrat",Arial,sans-serif;font-weight:700;font-size:14px;color:var(--teal);line-height:1.65;text-transform:uppercase}
.features li::before{content:"✓ ";color:var(--orange)}
.col--how{left:60px;top:600px;width:1000px}
.col--quote{left:60px;top:800px;width:1000px;text-align:right}
.quote{font-style:italic;font-size:14px;line-height:1.5;text-align:left}
.quote-name{font-style:italic;font-weight:600;margin-top:10px}

.footer{position:absolute;left:0;bottom:0;width:100%;display:flex}
.flyer--main .footer{height:170px}
.footer__from{flex:0 0 30%;background:var(--yellow);padding:22px 28px;font-size:13px;line-height:1.45}
.footer__from em{font-family:"Montserrat",Arial,sans-serif;font-style:italic;font-weight:700;font-size:17px;display:block;margin-bottom:4px}
.brand{display:flex;align-items:center;gap:8px;font-family:"Montserrat",Arial,sans-serif;font-weight:800;color:var(--teal-dark);font-size:18px;margin-top:8px}
.brand__dot{width:14px;height:14px;background:var(--teal-dark);border-radius:50%}
.footer__register{flex:1;background:#fff;padding:26px 30px;font-size:13px;line-height:1.5;color:var(--teal-dark)}
.footer__register strong{font-family:"Montserrat",Arial,sans-serif;font-size:15px;display:block}
.footer__id{flex:0 0 22%;background:var(--teal);color:#fff;padding:26px 24px;font-size:14px;line-height:1.8}

/* mini flyers */
.flyer--mini{width:540px;height:560px}
.flyer--mini .photo{height:230px}
.flyer--mini .enjoy{left:26px;top:22px;font-size:64px;letter-spacing:2px}
.flyer--mini .ribbon{left:22px;top:96px;min-width:230px;height:34px;padding:0 14px;font-size:14px;color:#fff;background:var(--accent)}
.flyer--mini .badge{right:26px;top:22px;width:118px;height:118px;font-size:9px;line-height:1.3;padding:14px;background:var(--accent2)}
.mini-cols{position:absolute;left:26px;top:245px;width:488px;display:flex;gap:24px}
.mini-cols>div{flex:1}
.flyer--mini .section-title{font-size:9px;color:var(--accent2);margin-bottom:3px}
.flyer--mini .body-text{font-size:8px;line-height:1.45;margin-bottom:8px}
.flyer--mini .features{font-size:8px;line-height:1.55;color:var(--accent2)}
.flyer--mini .footer{height:88px}
.flyer--mini .footer__from{background:var(--accent);color:#fff;padding:12px 14px;font-size:8px}
.flyer--mini .footer__from em{font-size:10px}
.flyer--mini .brand{font-size:10px;color:#fff;margin-top:4px}
.flyer--mini .brand__dot{width:8px;height:8px;background:#fff}
.flyer--mini .footer__register{padding:14px;font-size:8px;color:var(--accent2);background:linear-gradient(90deg,#fff,#eef1f4)}
.flyer--mini .footer__register strong{font-size:9px}
.flyer--mini .footer__id{background:var(--accent2);padding:14px;font-size:8px}

.m1{left:40px;top:1220px;--accent:var(--purple);--accent2:var(--orange)}
.m2{left:620px;top:1220px;--accent:var(--navy);--accent2:var(--sea)}
.m3{left:40px;top:1810px;--accent:var(--purple);--accent2:var(--teal)}
.m4{left:620px;top:1810px;--accent:var(--burgundy);--accent2:var(--navy)}
.m5{left:40px;top:2400px;--accent:var(--navy);--accent2:var(--red)}
.m6{left:620px;top:2400px;--accent:var(--burgundy);--accent2:var(--orange)}
.m1 .photo{background:linear-gradient(135deg,#c9a07a,#8a5a3a 50%,#e8d3b8)}
.m2 .photo{background:linear-gradient(180deg,#9fd3ee,#4b9fd0 55%,#dbe9f1)}
.m3 .photo{background:linear-gradient(180deg,#8fd8ec,#2fb0c4 55%,#f1e6cf)}
.m4 .photo{background:linear-gradient(135deg,#d9c3b2,#a8705a 50%,#f3e7dc)}
.m5 .photo{background:linear-gradient(180deg,#a7c8e8,#6a8fc0 50%,#d7c6b0)}
.m6 .photo{background:linear-gradient(180deg,#f4b27a,#d96b5a 45%,#6e8fb8)}
</style>
</head>
<body>

<section class="flyer flyer--main">
  <div class="photo" role="img" aria-label="Tropical beach with turquoise water and white sand">
    <svg class="photo__curve" viewBox="0 0 1120 200" preserveAspectRatio="none" height="200"><path d="M0 20 C 320 40 520 200 1120 170 L1120 200 L0 200 Z" fill="#fff"/></svg>
  </div>
  <div class="enjoy">ENJOY</div>
  <div class="ribbon">A 2 Night Hotel Stay</div>
  <div class="badge"><span><span class="badge__big">2+</span>Night Hotel Accommodations in the City of Your Choice at Over 50 of the Most Popular Destinations Available!</span></div>

  <div class="col col--plan">
    <h3 class="section-title">EXCLUSIVE PLAN:</h3>
    <p class="body-text">Thanks to an offer that welcomes a hotel stay, you can enjoy a relaxing vacation for just yourself and your loved ones. Enjoy two nights at the hotel of your choice in the city of your choice at one of over 50 of the most popular vacation spots around the country. Thanks to the business you received this certificate from, your stay is free — enjoy a nice break from routine.</p>
  </div>

  <div class="col col--features">
    <h3 class="section-title">FEATURES:</h3>
    <ul class="features">
      <li>Travel 7 days a week</li>
      <li>Good for two adults and children</li>
      <li>No hotel taxes or resort fees</li>
      <li>Stay through the 2+ night certificate</li>
      <li>Your choice of over 50 popular destinations</li>
      <li>Pay just the taxes and fees</li>
      <li>Fully transferable to another person</li>
      <li>18 months to complete travel after redemption</li>
    </ul>
  </div>

  <div class="col col--how">
    <h3 class="section-title">HOW CAN WE DO THIS:</h3>
    <p class="body-text">We contract with the world's leading hotel chains and resorts to have them fill their otherwise empty rooms. We help fill empty rooms which the hotels, resorts and cruise lines turn into additional revenue from other areas of their property and future bookings. Hotels rarely experience full occupancy, yet they remain open, providing rooms and services at fixed costs. So when hotels give out their rooms by partnering with marketing companies like us, they might miss out on the room fee, but they already didn't have that in the first place, at least now they have the opportunity to gain a customer for their in-house restaurants, room service, their casinos, and also future bookings, etc.</p>
  </div>

  <div class="col col--quote">
    <h3 class="section-title">WHAT OTHERS SAY</h3>
    <p class="quote">"Being able to stay right on the strip in Las Vegas was great. Your trip was easy to book and I would go again. We would recommend this offer to anyone looking for a well-deserved getaway with family. Thank you so much for the wonderful stay — we loved the atmosphere and the food! The whole experience was awesome. THANK YOU!"</p>
    <p class="quote-name">Marisa L. Portland, OR</p>
  </div>

  <div class="footer">
    <div class="footer__from">
      <em>Compliments of:</em>
      Alex Moreno<br>555-0142 · Sales Office<br>alex@harborline.example
      <div class="brand"><span class="brand__dot"></span>Harborline</div>
    </div>
    <div class="footer__register">
      <strong>REGISTER ALL THE DETAILS OF THIS SPECIAL OFFER AND REDEEM ONLINE AT:</strong>
      www.staywellvoucher.com<br>
      Terms and conditions apply; see website for full details.
    </div>
    <div class="footer__id">Certificate ID:<br>_______________<br>Expiration:<br>_______________</div>
  </div>
</section>

<!-- Series: six variants -->
<section class="flyer flyer--mini m1">
  <div class="photo" role="img" aria-label="Luxury resort lobby interior"><svg class="photo__curve" viewBox="0 0 540 80" preserveAspectRatio="none" height="80"><path d="M0 10 C 150 20 260 80 540 70 L540 80 L0 80 Z" fill="#fff"/></svg></div>
  <div class="enjoy">ENJOY</div>
  <div class="ribbon">A 7 Night Luxury Resort Stay</div>
  <div class="badge"><span>7 Nights at a Luxury Resort in Top Destinations!</span></div>
  <div class="mini-cols">
    <div><h3 class="section-title">EXCLUSIVE PLAN:</h3><p class="body-text">Relax for seven nights at a premium resort chosen from a list of favorite vacation spots, with comfort and service included.</p><h3 class="section-title">HOW CAN WE DO THIS:</h3><p class="body-text">Resorts partner with us to fill open rooms and welcome new guests who enjoy their dining and spa.</p></div>
    <div><h3 class="section-title">FEATURES:</h3><ul class="features"><li>Travel 7 days a week</li><li>Good for two adults</li><li>Fully transferable</li><li>18 months to travel</li></ul></div>
  </div>
  <div class="footer"><div class="footer__from"><em>Compliments of:</em>Alex Moreno<div class="brand"><span class="brand__dot"></span>Harborline</div></div><div class="footer__register"><strong>REDEEM ONLINE AT:</strong>www.staywellvoucher.com</div><div class="footer__id">Certificate ID:<br>Expiration:</div></div>
</section>

<section class="flyer flyer--mini m2">
  <div class="photo" role="img" aria-label="Cruise ship on open blue sea"><svg class="photo__curve" viewBox="0 0 540 80" preserveAspectRatio="none" height="80"><path d="M0 10 C 150 20 260 80 540 70 L540 80 L0 80 Z" fill="#fff"/></svg></div>
  <div class="enjoy">ENJOY</div>
  <div class="ribbon">A 4 Night Luxury Travel Getaway</div>
  <div class="badge"><span>4 Nights of Travel to Sunny Ports of Call!</span></div>
  <div class="mini-cols">
    <div><h3 class="section-title">EXCLUSIVE PLAN:</h3><p class="body-text">Sail away for four nights with cabin stay, meals on board and entertainment for you and a guest.</p><h3 class="section-title">HOW CAN WE DO THIS:</h3><p class="body-text">Cruise lines fill open cabins and earn from onboard services and future bookings.</p></div>
    <div><h3 class="section-title">FEATURES:</h3><ul class="features"><li>Meals included</li><li>Good for two adults</li><li>Fully transferable</li><li>18 months to travel</li></ul></div>
  </div>
  <div class="footer"><div class="footer__from"><em>Compliments of:</em>Alex Moreno<div class="brand"><span class="brand__dot"></span>Harborline</div></div><div class="footer__register"><strong>REDEEM ONLINE AT:</strong>www.staywellvoucher.com</div><div class="footer__id">Certificate ID:<br>Expiration:</div></div>
</section>

<section class="flyer flyer--mini m3">
  <div class="photo" role="img" aria-label="Island lagoon with overwater bungalows"><svg class="photo__curve" viewBox="0 0 540 80" preserveAspectRatio="none" height="80"><path d="M0 10 C 150 20 260 80 540 70 L540 80 L0 80 Z" fill="#fff"/></svg></div>
  <div class="enjoy">ENJOY</div>
  <div class="ribbon">Boat Cruise</div>
  <div class="badge"><span>A Relaxing Cruise Getaway for Two!</span></div>
  <div class="mini-cols">
    <div><h3 class="section-title">EXCLUSIVE PLAN:</h3><p class="body-text">Enjoy a cruise with ocean views, warm beaches and time to unwind with the people you love.</p><h3 class="section-title">HOW CAN WE DO THIS:</h3><p class="body-text">Partners offer open space to new guests who return and book again.</p></div>
    <div><h3 class="section-title">FEATURES:</h3><ul class="features"><li>Popular departure ports</li><li>Good for two adults</li><li>Fully transferable</li><li>18 months to travel</li></ul></div>
  </div>
  <div class="footer"><div class="footer__from"><em>Compliments of:</em>Alex Moreno<div class="brand"><span class="brand__dot"></span>Harborline</div></div><div class="footer__register"><strong>REDEEM ONLINE AT:</strong>www.staywellvoucher.com</div><div class="footer__id">Certificate ID:<br>Expiration:</div></div>
</section>

<section class="flyer flyer--mini m4">
  <div class="photo" role="img" aria-label="Couple dining at a restaurant table"><svg class="photo__curve" viewBox="0 0 540 80" preserveAspectRatio="none" height="80"><path d="M0 10 C 150 20 260 80 540 70 L540 80 L0 80 Z" fill="#fff"/></svg></div>
  <div class="enjoy">ENJOY</div>
  <div class="ribbon">Dining Rewards</div>
  <div class="badge"><span>Savings at Restaurants Near You!</span></div>
  <div class="mini-cols">
    <div><h3 class="section-title">EXCLUSIVE PLAN:</h3><p class="body-text">Treat yourself to meals out at participating restaurants with savings on every visit.</p><h3 class="section-title">HOW CAN WE DO THIS:</h3><p class="body-text">Restaurants gain new regular guests when they share open tables with us.</p></div>
    <div><h3 class="section-title">FEATURES:</h3><ul class="features"><li>Many local choices</li><li>Use any day</li><li>Fully transferable</li><li>12 months to use</li></ul></div>
  </div>
  <div class="footer"><div class="footer__from"><em>Compliments of:</em>Alex Moreno<div class="brand"><span class="brand__dot"></span>Harborline</div></div><div class="footer__register"><strong>REDEEM ONLINE AT:</strong>www.staywellvoucher.com</div><div class="footer__id">Certificate ID:<br>Expiration:</div></div>
</section>

<section class="flyer flyer--mini m5">
  <div class="photo" role="img" aria-label="European city skyline with a landmark tower"><svg class="photo__curve" viewBox="0 0 540 80" preserveAspectRatio="none" height="80"><path d="M0 10 C 150 20 260 80 540 70 L540 80 L0 80 Z" fill="#fff"/></svg></div>
  <div class="enjoy">ENJOY</div>
  <div class="ribbon">International Hotel Stay</div>
  <div class="badge"><span>Hotel Nights in Cities Around the World!</span></div>
  <div class="mini-cols">
    <div><h3 class="section-title">EXCLUSIVE PLAN:</h3><p class="body-text">Stay in famous cities abroad with hotel nights covered so you can explore at your own pace.</p><h3 class="section-title">HOW CAN WE DO THIS:</h3><p class="body-text">Hotels welcome new guests to open rooms and gain future visitors.</p></div>
    <div><h3 class="section-title">FEATURES:</h3><ul class="features"><li>Global destinations</li><li>Good for two adults</li><li>Fully transferable</li><li>18 months to travel</li></ul></div>
  </div>
  <div class="footer"><div class="footer__from"><em>Compliments of:</em>Alex Moreno<div class="brand"><span class="brand__dot"></span>Harborline</div></div><div class="footer__register"><strong>REDEEM ONLINE AT:</strong>www.staywellvoucher.com</div><div class="footer__id">Certificate ID:<br>Expiration:</div></div>
</section>

<section class="flyer flyer--mini m6">
  <div class="photo" role="img" aria-label="City strip at sunset with hotel lights"><svg class="photo__curve" viewBox="0 0 540 80" preserveAspectRatio="none" height="80"><path d="M0 10 C 150 20 260 80 540 70 L540 80 L0 80 Z" fill="#fff"/></svg></div>
  <div class="enjoy">ENJOY</div>
  <div class="ribbon">A 3 Night Las Vegas Stay</div>
  <div class="badge"><span>3 Nights on the Famous Strip!</span></div>
  <div class="mini-cols">
    <div><h3 class="section-title">EXCLUSIVE PLAN:</h3><p class="body-text">Spend three nights in the heart of the city with shows, dining and lights all around you.</p><h3 class="section-title">HOW CAN WE DO THIS:</h3><p class="body-text">Hotels fill open rooms and earn from dining, shows and future visits.</p></div>
    <div><h3 class="section-title">FEATURES:</h3><ul class="features"><li>Travel 7 days a week</li><li>Good for two adults</li><li>Fully transferable</li><li>18 months to travel</li></ul></div>
  </div>
  <div class="footer"><div class="footer__from"><em>Compliments of:</em>Alex Moreno<div class="brand"><span class="brand__dot"></span>Harborline</div></div><div class="footer__register"><strong>REDEEM ONLINE AT:</strong>www.staywellvoucher.com</div><div class="footer__id">Certificate ID:<br>Expiration:</div></div>
</section>

</body>
</html>
```